8 x 8 Social Media Design - Crest Pathway #1

Why be a regular Agent, when you can be a Boss?
MOVA PRIMEHOLD REALTY GROUP
We offer Four Levels of Participation
You Increase your Earning Potential at Each Level
Level One - Learn to Earn Additional Income Through....
Mortgage Originations - Dual Licensing / No Additional Work
Real Estate Investing - Invest Jointly with Us
Agent Recruitment - Up to 10% Override
Level Two - Team Leader
Level Three - Minority Mova Franchise Ownership
Level Four - Majority Mova Franchise Ownership
For more information visit us at www.careersatmovaprmhold.example and request a meeting with our Managing Broker, Mr. Harold Tismeer.

```html
<!DOCTYPE html>
<html lang="en">
<head>
<meta charset="utf-8">
<title>Social Media Design – Crest Pathway #1</title>
<link rel="stylesheet" href="https://fonts.googleapis.com/css2?family=Montserrat:wght@300;400;500;600;700;800;900&display=swap">
<style>
  :root {
    --page: #ffffff;
    --board: #d2d3d5;
    --paper: #efefee;
    --navy: #0d2d4f;
    --gold: #8c7b47;
    --blue: #1c5d9a;
    --teal: #1f8f96;
    --white: #ffffff;
    --badge-rim: #dde0e4;
  }
  * { margin: 0; padding: 0; box-sizing: border-box; }
  html, body { width: 918px; height: 1200px; overflow: hidden; background: var(--page); }
  body { font-family: "Montserrat", Arial, sans-serif; }
  .stage { position: relative; width: 918px; height: 1200px; overflow: hidden; }
  .board { position: absolute; left: 28px; top: 26px; width: 860px; height: 1143px; background: var(--board); }
  .abs { position: absolute; line-height: 1; white-space: nowrap; }

  .board-title { left: 78px; top: 83px; font-size: 52px; font-weight: 700; color: var(--white); letter-spacing: -0.5px; }
  .board-subtitle { left: 78px; top: 133px; font-size: 52px; font-weight: 300; color: var(--white); letter-spacing: -0.5px; }

  .post { position: absolute; left: 76px; top: 237px; width: 767px; height: 766px; background: var(--paper); box-shadow: 3px 4px 8px rgba(0,0,0,0.28); overflow: hidden; }

  .headline-lead { left: 134px; top: 269px; font-size: 30px; font-weight: 400; color: var(--navy); }
  .headline-main { left: 133px; top: 302px; font-size: 36px; font-weight: 800; color: var(--navy); }
  .headline-boss { left: 128px; top: 331px; font-size: 106px; font-weight: 900; color: var(--gold); letter-spacing: -7px; }

  .brand { position: absolute; left: 612px; top: 272px; width: 176px; text-align: center; }
  .brand-mark { width: 36px; height: 36px; background: var(--teal); margin: 0 auto 38px; }
  .brand-name { font-size: 11.5px; font-weight: 600; color: var(--navy); white-space: nowrap; }

  .photo-strip { position: absolute; left: 76px; top: 424px; width: 767px; height: 153px; display: flex; }
  .photo { flex: 1; height: 100%; }
  .photo--1 { background: linear-gradient(160deg, #d8d4cf, #5a3d2e 55%, #2a2a2e); }
  .photo--2 { background: linear-gradient(160deg, #1f6f73, #1f2a4a 55%, #141416); }
  .photo--3 { background: linear-gradient(160deg, #3a2e25, #24242a 55%, #121214); }
  .photo--4 { background: linear-gradient(160deg, #6f8a4e, #4b6d92 60%, #3b4f6a); }
  .photo--5 { background: linear-gradient(160deg, #dfe3e8, #9aa3ad 50%, #1c1c20); }

  .strip-caption { left: 134px; top: 562px; font-size: 16.5px; font-weight: 700; color: var(--white); }
  .earning-line { left: 247px; top: 582px; font-size: 17.5px; font-weight: 700; color: var(--navy); }

  .badge { position: absolute; width: 93px; height: 115px; }
  .badge--1 { left: 150px; top: 601px; }
  .badge--2 { left: 150px; top: 730px; }
  .badge--3 { left: 399px; top: 730px; }
  .badge--4 { left: 648px; top: 730px; }

  .level-intro { left: 268px; top: 622px; font-size: 16.5px; font-weight: 600; color: var(--navy); }
  .level-row { position: absolute; left: 268px; font-size: 13px; line-height: 1; white-space: nowrap; color: var(--navy); }
  .level-row .method { position: absolute; left: 0; color: var(--gold); }
  .level-row .detail { position: absolute; left: 164px; }
  .level-row .detail::before { content: "•"; position: absolute; left: -11px; }
  .level-row--1 { top: 646px; }
  .level-row--2 { top: 665px; }
  .level-row--3 { top: 684px; }

  .level-label { position: absolute; font-size: 16.5px; font-weight: 600; color: var(--navy); text-align: center; line-height: 19px; width: 240px; }
  .level-label--2 { left: 74px; top: 862px; }
  .level-label--3 { left: 325px; top: 851px; }
  .level-label--4 { left: 574px; top: 851px; }

  .divider { position: absolute; top: 729px; width: 2px; height: 161px; background: var(--gold); }
  .divider--a { left: 319px; }
  .divider--b { left: 569px; }

  .footer { position: absolute; left: 76px; top: 904px; width: 767px; height: 99px; background: var(--navy); color: var(--white); text-align: center; }
  .footer-intro { position: absolute; left: 0; right: 0; top: 15px; font-size: 13px; font-weight: 400; }
  .footer-url { position: absolute; left: 0; right: 0; top: 31px; font-size: 24px; font-weight: 400; color: var(--gold); }
  .footer-url strong { font-weight: 700; }
  .footer-cta { position: absolute; left: 0; right: 0; top: 63px; font-size: 13px; font-weight: 400; }
  .footer-cta strong { font-weight: 700; }
</style>
</head>
<body>
<div class="stage">
  <div class="board"></div>
  <h1 class="abs board-title">Social Media Design</h1>
  <p class="abs board-subtitle">Crest Pathway #1</p>

  <div class="post"></div>

  <p class="abs headline-lead">Why be a Regular Agent</p>
  <p class="abs headline-main">When you can be a</p>
  <p class="abs headline-boss">BOSS ?</p>

  <div class="brand">
    <div class="brand-mark"></div>
    <p class="brand-name">MOVA PRIMEHOLD REALTY GROUP</p>
  </div>

  <div class="photo-strip">
    <div class="photo photo--1" role="img" aria-label="Portrait of a smiling agent in a dark blazer"></div>
    <div class="photo photo--2" role="img" aria-label="Agent in a blue suit and red tie against a teal lettering backdrop"></div>
    <div class="photo photo--3" role="img" aria-label="Two agents posed in a dark library office"></div>
    <div class="photo photo--4" role="img" aria-label="Agent in a denim shirt outdoors with greenery"></div>
    <div class="photo photo--5" role="img" aria-label="Agent in a black hat and coat on a light backdrop"></div>
  </div>

  <p class="abs strip-caption">WE OFFER FOUR LEVELS OF PARTICIPATION</p>
  <p class="abs earning-line">YOU INCREASE YOUR EARNING POTENTIAL AT EACH LEVEL</p>

  <svg class="badge badge--1" viewBox="0 0 100 124" aria-hidden="true">
    <polygon points="50,0 100,28 100,96 50,124 0,96 0,28" fill="var(--badge-rim)"/>
    <polygon points="50,6 94,31 94,93 50,118 6,93 6,31" fill="var(--blue)"/>
    <polygon points="50,6 94,31 50,45 6,62 6,31" fill="var(--navy)"/>
    <text x="14" y="52" transform="rotate(-28 14 52)" font-family="Montserrat, sans-serif" font-size="13" font-weight="500" fill="#fff">LEVEL</text>
    <text x="68" y="42" font-family="Montserrat, sans-serif" font-size="30" font-weight="800" fill="#fff">1</text>
    <polygon points="50,44 84,62 84,98 50,118 16,98 16,62" fill="#b09a80" role="img" aria-label="Colleagues meeting around a desk"/>
  </svg>

  <p class="abs level-intro">Learn to Earn Additional Income Through....</p>
  <div class="level-row level-row--1"><span class="method">Mortgage Originations</span><span class="detail">Dual Licensing &nbsp;&nbsp;|&nbsp; No Additional Work</span></div>
  <div class="level-row level-row--2"><span class="method">Real Estate Investing</span><span class="detail">Invest Jointly with Us</span></div>
  <div class="level-row level-row--3"><span class="method">Agent Recruitment</span><span class="detail">Up to 10% Override</span></div>

  <svg class="badge badge--2" viewBox="0 0 100 124" aria-hidden="true">
    <polygon points="50,0 100,28 100,96 50,124 0,96 0,28" fill="var(--badge-rim)"/>
    <polygon points="50,6 94,31 94,93 50,118 6,93 6,31" fill="var(--blue)"/>
    <polygon points="50,6 94,31 50,45 6,62 6,31" fill="var(--navy)"/>
    <text x="14" y="52" transform="rotate(-28 14 52)" font-family="Montserrat, sans-serif" font-size="13" font-weight="500" fill="#fff">LEVEL</text>
    <text x="66" y="42" font-family="Montserrat, sans-serif" font-size="30" font-weight="800" fill="#fff">2</text>
    <polygon points="50,44 84,62 84,98 50,118 16,98 16,62" fill="#7a5a40" role="img" aria-label="Team hands joined together"/>
  </svg>

  <svg class="badge badge--3" viewBox="0 0 100 124" aria-hidden="true">
    <polygon points="50,0 100,28 100,96 50,124 0,96 0,28" fill="var(--badge-rim)"/>
    <polygon points="50,6 94,31 94,93 50,118 6,93 6,31" fill="var(--blue)"/>
    <polygon points="50,6 94,31 50,45 6,62 6,31" fill="var(--navy)"/>
    <text x="14" y="52" transform="rotate(-28 14 52)" font-family="Montserrat, sans-serif" font-size="13" font-weight="500" fill="#fff">LEVEL</text>
    <text x="66" y="42" font-family="Montserrat, sans-serif" font-size="30" font-weight="800" fill="#fff">3</text>
    <polygon points="50,44 84,62 84,98 50,118 16,98 16,62" fill="#6a4a3c" role="img" aria-label="Business owners talking in a shop"/>
  </svg>

  <svg class="badge badge--4" viewBox="0 0 100 124" aria-hidden="true">
    <polygon points="50,0 100,28 100,96 50,124 0,96 0,28" fill="var(--badge-rim)"/>
    <polygon points="50,6 94,31 94,93 50,118 6,93 6,31" fill="var(--blue)"/>
    <polygon points="50,6 94,31 50,45 6,62 6,31" fill="var(--navy)"/>
    <text x="14" y="52" transform="rotate(-28 14 52)" font-family="Montserrat, sans-serif" font-size="13" font-weight="500" fill="#fff">LEVEL</text>
    <text x="66" y="42" font-family="Montserrat, sans-serif" font-size="30" font-weight="800" fill="#fff">4</text>
    <polygon points="50,44 84,62 84,98 50,118 16,98 16,62" fill="#a89484" role="img" aria-label="Business partners in conversation"/>
  </svg>

  <p class="level-label level-label--2">Team Leader</p>
  <p class="level-label level-label--3">Minority Mova<br>Franchise Ownership</p>
  <p class="level-label level-label--4">Majority Mova<br>Franchise Ownership</p>

  <div class="divider divider--a"></div>
  <div class="divider divider--b"></div>

  <footer class="footer">
    <p class="footer-intro">For more information visit us at</p>
    <p class="footer-url">www.<strong>careersatmovaprmhold</strong>.example</p>
    <p class="footer-cta">and request a meeting with our Managing Broker <strong>| Mr. Harold Tismeer</strong>.</p>
  </footer>
</div>
</body>
</html>
```